Psychotherapist need a business card with logo

I am a psychotherapist in need of a business card. The card must have:

Moravia Telvundor
Psicoterapeuta
937 218 604

Psychologists use the greek letter psy, which is the psychologist symbol, but I would prefer something like a mandala, a graphic symbol, an iconic tree, nothing very usual, but something that shows confidence and trust.

Industry/Entity Type

Business

```html
<!DOCTYPE html>
<html lang="es">
<head>
<meta charset="utf-8">
<title>Moravia Telvundor – Psicoterapeuta</title>
<link rel="stylesheet" href="https://fonts.googleapis.com/css2?family=Exo+2:wght@300;400&display=swap">
<style>
  :root {
    --page-bg: #ffffff;
    --card-bg: #ffffff;
    --card-edge: #d6d6d6;
    --card-shadow: #c8c6c7;
    --teal: #73b5a8;
    --cream: #ebebc2;
    --mark-shadow: #cfcdce;
  }
  html, body {
    margin: 0;
    padding: 0;
    width: 1200px;
    height: 1000px;
    overflow: hidden;
    background: var(--page-bg);
  }
  .canvas {
    position: relative;
    width: 1200px;
    height: 1000px;
    font-family: "Exo 2", sans-serif;
  }
  .business-card {
    position: absolute;
    left: 215px;
    top: 140px;
    width: 646px;
    height: 359px;
    background: var(--card-bg);
    border: 1px solid var(--card-edge);
    box-sizing: border-box;
    box-shadow: 24px 26px 0 0 var(--card-shadow);
  }
  .holder-name {
    position: absolute;
    left: 15px;
    top: 44px;
    margin: 0;
    font-weight: 300;
    font-size: 37px;
    line-height: 1;
    color: var(--teal);
    white-space: nowrap;
  }
  .name-rule {
    position: absolute;
    left: 33px;
    top: 98px;
    width: 265px;
    height: 2px;
    background: var(--teal);
  }
  .holder-role {
    position: absolute;
    left: 56px;
    top: 104px;
    margin: 0;
    font-weight: 300;
    font-size: 29px;
    line-height: 1.1;
    color: var(--teal);
  }
  .contact-phone {
    position: absolute;
    left: 17px;
    top: 300px;
    display: flex;
    align-items: center;
    gap: 18px;
    font-weight: 300;
    font-size: 32px;
    color: var(--teal);
  }
  .contact-phone svg { display: block; }
  .brand-mark {
    position: absolute;
    left: 359px;
    top: 70px;
    width: 220px;
    height: 220px;
    border-radius: 50%;
    background: var(--cream);
    box-shadow: 8px 12px 0 0 var(--mark-shadow);
    display: flex;
    align-items: center;
    justify-content: center;
  }
  .brand-name {
    font-weight: 300;
    font-size: 32px;
    line-height: 1;
    color: var(--teal);
  }
</style>
</head>
<body>
<main class="canvas">
  <section class="business-card" aria-label="Tarjeta de presentación">
    <h1 class="holder-name">Moravia Telvundor</h1>
    <div class="name-rule"></div>
    <p class="holder-role">Psicoterapeuta</p>

    <div class="brand-mark">
      <span class="brand-name">Telvundor</span>
    </div>

    <div class="contact-phone">
      <svg width="20" height="32" viewBox="0 0 20 32" aria-hidden="true">
        <rect x="1.5" y="1.5" width="17" height="29" rx="3" fill="none" stroke="var(--teal)" stroke-width="3"/>
        <rect x="5" y="5" width="10" height="18" fill="var(--teal)" opacity="0.35"/>
        <circle cx="10" cy="26.5" r="1.6" fill="var(--teal)"/>
      </svg>
      <span class="phone-number">937 218 604</span>
    </div>
  </section>
</main>
</body>
</html>
```